Harvest Moon's Riddle Event Flyer - Fundraiser for a High Council Candidate

Working on an event flyer for a fundraiser for a Verdantist candidate for Council in Tennessee. Hosting an event for him that's a Harvest Moon's Riddle theme, and I need a cool flyer that fits the theme with event details.
Host names will be added to the flyer on an ongoing basis, so will need someone who can quickly add names to flyer as hosts commit. Would like to agree to a fee for all work up front.
I'm attaching a mockup of a flyer that my friend did, before he had to back out because of work commitments, as well as a couple of pieces of Harvest Moon's Riddle art that I think are cool.
Verdantist

```html
<!DOCTYPE html>
<html lang="en">
<head>
<meta charset="utf-8">
<title>A Harvest Moon's VNC Meeting Eve – Reception Flyer</title>
<link rel="stylesheet" href="https://fonts.googleapis.com/css2?family=Dancing+Script:wght@700&family=Noto+Serif:ital,wght@1,400;1,700&family=Mulish:wght@400;700&display=swap">
<style>
  :root {
    --page-bg: #2a2a2c;
    --sky-top: #0c1729;
    --sky-mid: #1d3552;
    --sky-bottom: #05080d;
    --ink-navy: #13283a;
    --title-outline: #ffffff;
    --text-light: #f2f4f7;
    --moon-light: #e9eaec;
    --moon-shade: #a9acb1;
  }
  * { margin: 0; padding: 0; box-sizing: border-box; }
  html, body {
    width: 1200px; height: 1200px; overflow: hidden;
    background: var(--page-bg);
  }
  .flyer {
    position: absolute;
    left: 219px; top: 106px;
    width: 763px; height: 988px;
    overflow: hidden;
    background: linear-gradient(180deg, var(--sky-top) 0%, var(--sky-mid) 45%, #132538 68%, var(--sky-bottom) 100%);
  }
  .flyer-art { position: absolute; inset: 0; }
  .title-art { position: absolute; inset: 0; }
  .title-script {
    font-family: 'Dancing Script', cursive;
    font-weight: 700;
    fill: var(--ink-navy);
    stroke: var(--title-outline);
    stroke-width: 7px;
    paint-order: stroke;
    stroke-linejoin: round;
  }
  .invite-line {
    font-family: 'Noto Serif', serif;
    font-style: italic;
    font-size: 21px;
    fill: var(--ink-navy);
    letter-spacing: 0.5px;
  }
  .event-details {
    position: absolute;
    left: 0; right: 0; top: 680px;
    text-align: center;
    color: var(--text-light);
    font-family: 'Noto Serif', serif;
    font-style: italic;
  }
  .event-details .reception,
  .event-details .when { font-size: 27px; line-height: 42px; }
  .event-details .guest { font-weight: 700; }
  .event-details .venue { margin-top: 28px; font-size: 23px; line-height: 34px; }
  .paid-for {
    position: absolute;
    left: 186px; top: 911px;
    display: flex; align-items: center; gap: 22px;
    color: var(--text-light);
    font-family: 'Mulish', sans-serif;
    font-size: 18px;
    letter-spacing: 0.6px;
  }
  .campaign-name { font-weight: 400; font-size: 15px; letter-spacing: 1.5px; text-transform: uppercase; }
</style>
</head>
<body>
  <main class="flyer">
    <svg class="flyer-art" width="763" height="988" viewBox="0 0 763 988" role="img" aria-label="Night sky with stars, a large glowing full moon, and dark mountain ridges below">
      <defs>
        <radialGradient id="moonGlow" cx="422" cy="346" r="420" gradientUnits="userSpaceOnUse">
          <stop offset="0.7" stop-color="#8fa6bd" stop-opacity="0.55"/>
          <stop offset="1" stop-color="#1d3552" stop-opacity="0"/>
        </radialGradient>
        <radialGradient id="moonFace" cx="400" cy="320" r="310" gradientUnits="userSpaceOnUse">
          <stop offset="0" stop-color="var(--moon-light)"/>
          <stop offset="0.75" stop-color="#cfd1d4"/>
          <stop offset="1" stop-color="var(--moon-shade)"/>
        </radialGradient>
        <linearGradient id="ridge" x1="0" y1="0" x2="0" y2="1">
          <stop offset="0" stop-color="#1a2f44"/>
          <stop offset="1" stop-color="#04070b"/>
        </linearGradient>
      </defs>
      <circle cx="422" cy="346" r="420" fill="url(#moonGlow)"/>
      <circle cx="422" cy="346" r="305" fill="url(#moonFace)"/>
      <rect x="0" y="600" width="763" height="388" fill="url(#ridge)" opacity="0.85"/>
    </svg>

    <svg class="title-art" width="763" height="988" viewBox="0 0 763 988">
      <defs>
        <path id="inviteArc" d="M 190 300 Q 330 150 520 180"/>
      </defs>
      <text class="invite-line"><textPath href="#inviteArc">You’re cordially invited to</textPath></text>
      <text class="title-script" x="300" y="340" font-size="110">A</text>
      <text class="title-script" x="395" y="455" font-size="96" text-anchor="middle">Harvest Moon’s</text>
      <text class="title-script" x="440" y="522" font-size="46" text-anchor="middle" transform="rotate(-6 440 522)">VNC Meeting Eve.</text>
    </svg>

    <section class="event-details">
      <p class="reception">Reception for <span class="guest">Jonah Hartwell</span></p>
      <p class="when">Wednesday, August 23rd 6-9p.m.</p>
      <p class="venue">House of Walter Brisby<br>418B Larkspur Ave, Nashville, TN 37216</p>
    </section>

    <footer class="paid-for">
      <span>Paid for by Hartwell for High Council</span>
      <span class="campaign-name">Jonah Hartwell</span>
    </footer>
  </main>
</body>
</html>
```